Thanksgiving Postcard with my family photo on front from my dental office

I just want to send out a Thaksgiving postcard of my family to patients at my dental practice: I want the entire front to be a photo of the family that I have downloaded. I want to get it done soon since Thanksgiving is here. 5x7 preferable

Industry/Entity Type

Dental

```html
<!DOCTYPE html>
<html lang="en">
<head>
<meta charset="utf-8">
<title>Thanksgiving Postcard Options</title>
<link rel="stylesheet" href="https://fonts.googleapis.com/css2?family=Allura&family=Josefin+Sans:wght@400;600&family=Quicksand:wght@500;600&family=Oswald:wght@500;600&family=Lobster&family=Great+Vibes&display=swap">
<style>
  :root {
    --page: #ffffff;
    --card-brown: #4b3a2f;
    --photo-green: #5f7a3e;
    --photo-warm: #b88a5a;
    --photo-red: #d9442e;
    --orange: #e3873a;
    --gold: #dba53e;
    --olive: #c9c46c;
    --cream: #fbf4e8;
    --coral: #e25d45;
    --red-dash: #c4463a;
    --teal: #2aa89a;
    --acorn: #e2a23e;
    --leaf: #c8b157;
  }
  * { box-sizing: border-box; margin: 0; padding: 0; }
  html, body { width: 1200px; height: 902px; overflow: hidden; background: var(--page); }
  .canvas { position: relative; width: 1200px; height: 902px; }

  .family-photo {
    position: absolute; left: 0; width: 589px; height: 422px;
    background:
      radial-gradient(ellipse 60% 45% at 50% 60%, rgba(217,68,46,.55), transparent 70%),
      linear-gradient(180deg, var(--photo-green) 0%, #8a9a5a 35%, var(--photo-warm) 60%, #3a2f2a 100%);
  }
  .family-photo.top { top: 0; }
  .family-photo.bottom { top: 480px; }

  .card-back {
    position: absolute; left: 607px; width: 593px; height: 422px;
    background: var(--card-brown); color: var(--cream); overflow: hidden;
  }
  .card-back.top { top: 0; }
  .card-back.bottom { top: 480px; }

  /* Option one */
  .headline-small {
    position: absolute; left: 36px; font-family: "Josefin Sans", sans-serif;
    font-size: 30px; letter-spacing: 1px; color: var(--orange); line-height: 1;
    z-index: 2;
  }
  .headline-small.line-one { top: 12px; }
  .headline-small.line-two { top: 44px; }
  .headline-script {
    position: absolute; left: 20px; top: 62px; font-family: "Allura", cursive;
    font-size: 112px; line-height: 1; color: var(--olive); z-index: 1;
  }
  .message {
    position: absolute; font-family: "Quicksand", sans-serif; font-weight: 500;
    text-align: center; line-height: 21px; font-size: 16.5px;
  }
  .message p + p { margin-top: 21px; }
  .option-one .message { left: 70px; width: 410px; top: 166px; }
  .option-one .sign-off {
    position: absolute; left: 110px; top: 360px; font-family: "Quicksand", sans-serif;
    font-weight: 500; font-size: 16.5px; white-space: nowrap;
  }
  .footer-line {
    position: absolute; font-family: "Quicksand", sans-serif; font-weight: 600; font-size: 16px;
    white-space: nowrap;
  }
  .option-one .footer-line { right: 22px; top: 398px; color: var(--gold); }

  .acorn-cluster { position: absolute; }
  .acorn-cluster.upper {
    left: 380px; top: 20px; width: 213px; height: 190px;
    background: radial-gradient(ellipse 55% 50% at 60% 50%, rgba(226,162,62,.75), rgba(200,177,87,.25) 60%, transparent 75%);
  }
  .acorn-cluster.lower {
    left: 430px; top: 250px; width: 163px; height: 140px;
    background: radial-gradient(ellipse 55% 50% at 60% 50%, rgba(226,162,62,.75), rgba(200,177,87,.25) 60%, transparent 75%);
  }
  .leaf-corner {
    position: absolute; left: 8px; top: 320px; width: 90px; height: 80px;
    background: radial-gradient(circle at 50% 50%, rgba(227,135,58,.85), rgba(227,135,58,.2) 60%, transparent 72%);
  }

  /* Option two */
  .dashed-frame {
    position: absolute; inset: 8px; border: 2px dashed var(--red-dash);
  }
  .crown-icon { position: absolute; left: 140px; top: 28px; }
  .ribbon { position: absolute; left: 38px; top: 68px; }
  .ribbon-label {
    position: absolute; left: 38px; top: 76px; width: 276px; text-align: center;
    font-family: "Lobster", cursive; font-size: 27px; color: var(--card-brown);
  }
  .greeting { position: absolute; left: 20px; width: 310px; text-align: center; line-height: 1; white-space: nowrap; }
  .greeting.a-very { top: 152px; font-family: "Oswald", sans-serif; font-weight: 500; font-size: 40px; color: var(--orange); }
  .greeting.happy {
    top: 206px; font-family: "Oswald", sans-serif; font-weight: 500; font-size: 50px; letter-spacing: 6px;
    color: transparent; -webkit-text-stroke: 2px var(--coral);
  }
  .greeting.thanksgiving { top: 262px; font-family: "Great Vibes", cursive; font-size: 60px; color: var(--gold); }
  .greeting.day { top: 326px; font-family: "Oswald", sans-serif; font-weight: 600; font-size: 40px; color: var(--coral); }
  .option-two .message { left: 330px; width: 258px; top: 32px; color: var(--orange); font-size: 16px; line-height: 22px; }
  .option-two .message p + p { margin-top: 22px; }
  .option-two .footer-line { left: 0; width: 593px; text-align: center; top: 386px; color: var(--teal); }
</style>
</head>
<body>
<div class="canvas">

  <div class="family-photo top" role="img" aria-label="Family portrait photo of five people in red shirts seated outdoors in front of autumn trees"></div>

  <section class="card-back top option-one">
    <div class="acorn-cluster upper" role="img" aria-label="Illustrated acorns and autumn leaves"></div>
    <div class="acorn-cluster lower" role="img" aria-label="Illustrated acorns and autumn leaves"></div>
    <div class="leaf-corner" role="img" aria-label="Illustrated orange maple leaf"></div>
    <div class="headline-script">Thanks</div>
    <div class="headline-small line-one">EAT, DRINK</div>
    <div class="headline-small line-two">&amp; GIVE</div>
    <div class="message">
      <p>As the holiday season is upon us,<br>there is no time more fitting to think about all<br>that we are grateful for and say thank you<br>to those who have made our progress possible.</p>
      <p>We truly appreciate your business and hope<br>that the holidays and the coming year will bring you<br>happiness and success.</p>
    </div>
    <div class="sign-off">Best wishes from your Bright Dental Family</div>
    <div class="footer-line">Bright Dental, Inc./1420 Harbor Rd/Bayview, AL 36500</div>
  </section>

  <div class="family-photo bottom" role="img" aria-label="Family portrait photo of five people in red shirts seated outdoors in front of autumn trees"></div>

  <section class="card-back bottom option-two">
    <div class="dashed-frame"></div>
    <svg class="crown-icon" width="40" height="28" viewBox="0 0 40 28" aria-hidden="true">
      <path d="M4 22 L2 6 L12 14 L20 2 L28 14 L38 6 L36 22 Z" fill="var(--teal)"/>
      <rect x="4" y="23" width="32" height="4" fill="var(--teal)"/>
    </svg>
    <svg class="ribbon" width="276" height="60" viewBox="0 0 276 60" aria-hidden="true">
      <polygon points="0,22 34,22 34,52 0,52 12,37" fill="#b8612a"/>
      <polygon points="276,22 242,22 242,52 276,52 264,37" fill="#b8612a"/>
      <polygon points="22,6 254,6 254,46 22,46" fill="var(--orange)"/>
    </svg>
    <div class="ribbon-label">I wish you</div>
    <div class="greeting a-very">A VERY</div>
    <div class="greeting happy">HAPPY</div>
    <div class="greeting thanksgiving">Thanksgiving</div>
    <div class="greeting day">DAY</div>
    <div class="message">
      <p>As the holiday season<br>is upon us, there is no time<br>more fitting to think about all<br>that we are grateful for<br>and say thank you<br>to those who have made<br>our progress possible.</p>
      <p>We truly appreciate<br>your business and hope<br>that the holidays and the<br>coming year will bring you<br>happiness and success.</p>
      <p>Best wishes from your<br>Bright Dental Family</p>
    </div>
    <div class="footer-line">Bright Dental, Inc./1420 Harbor Rd/Bayview, AL 36500</div>
  </section>

</div>
</body>
</html>
```